Business Card Design

Hoping for a black background business card, minimalistic design.
With the Marble Crest logo you created in white.

I would like to include:
My Name and title
Address (street address)
Reception: (phone number)
Fax: (fax number)
Reception: (email address)
Direct email: (email address)
Instagram: (ig handle)

```html
<!DOCTYPE html>
<html lang="en">
<head>
<meta charset="utf-8">
<title>Marble Crest — Business Card</title>
<link href="https://fonts.googleapis.com/css2?family=Montserrat:wght@500&family=Poppins:wght@400;500&display=swap" rel="stylesheet">
<style>
  :root {
    --stage: #1c1c1c;
    --card-black: #050505;
    --card-white: #ffffff;
    --ink-light: #ffffff;
    --ink-dark: #0a0a0a;
  }
  * { box-sizing: border-box; margin: 0; padding: 0; }
  html, body { width: 1200px; height: 1015px; overflow: hidden; background: var(--stage); }
  body { font-family: "Poppins", sans-serif; position: relative; }

  .card {
    position: absolute; left: 200px; width: 800px; height: 457px;
    background: var(--card-black); overflow: hidden;
  }
  .card--front { top: 36px; }
  .card--back { top: 522px; }

  .brand { display: flex; align-items: center; gap: 26px; }
  .brand__mark { width: 92px; height: 92px; border-radius: 50%; border: 5px solid currentColor; }
  .brand__divider { width: 1px; height: 104px; background: currentColor; }
  .brand__name {
    font-family: "Montserrat", sans-serif; font-weight: 500;
    font-size: 46px; letter-spacing: 5px; text-transform: uppercase;
  }

  .card--front .brand {
    position: absolute; left: 0; right: 0; top: 0; bottom: 0;
    justify-content: center; color: var(--ink-light);
  }

  .back__band {
    position: absolute; left: 0; top: 0; width: 100%; height: 178px;
    background: var(--card-white); color: var(--ink-dark);
    display: flex; align-items: center; padding-left: 90px;
  }
  .back__rule {
    position: absolute; left: 0; top: 186px; width: 100%; height: 3px;
    background: var(--card-white);
  }

  .person { position: absolute; left: 70px; top: 218px; color: var(--ink-light); }
  .person__name { font-weight: 500; font-size: 22px; letter-spacing: 1px; text-transform: uppercase; line-height: 1.1; }
  .person__title { font-size: 17px; line-height: 1.2; }

  .contact-list { position: absolute; left: 70px; top: 300px; list-style: none; color: var(--ink-light); }
  .contact-list li { display: flex; align-items: center; gap: 10px; font-size: 19px; line-height: 34px; }
  .icon {
    width: 24px; height: 24px; border: 1.5px solid var(--ink-light); border-radius: 50%;
    display: flex; align-items: center; justify-content: center; flex-shrink: 0;
  }
  .icon svg { width: 13px; height: 13px; fill: none; stroke: var(--ink-light); stroke-width: 1.6; }

  .address {
    position: absolute; right: 50px; top: 218px; text-align: right;
    color: var(--ink-light); font-size: 19px; line-height: 1.2;
  }
  .social {
    position: absolute; right: 50px; top: 300px; display: flex; align-items: center; gap: 10px;
    color: var(--ink-light); font-size: 19px;
  }
  .social__dot { width: 22px; height: 22px; border: 1.5px solid var(--ink-light); border-radius: 50%; }
</style>
</head>
<body>

  <section class="card card--front" aria-label="Card front">
    <div class="brand">
      <span class="brand__mark"></span>
      <span class="brand__divider"></span>
      <span class="brand__name">Marble Crest</span>
    </div>
  </section>

  <section class="card card--back" aria-label="Card back">
    <div class="back__band">
      <div class="brand">
        <span class="brand__mark"></span>
        <span class="brand__divider"></span>
        <span class="brand__name">Marble Crest</span>
      </div>
    </div>
    <div class="back__rule"></div>

    <div class="person">
      <p class="person__name">Daniel Reyes</p>
      <p class="person__title">Managing Director</p>
    </div>

    <ul class="contact-list">
      <li>
        <span class="icon"><svg viewBox="0 0 16 16"><path d="M4 2l2.5 3-1.5 1.5c.8 1.8 2.2 3.2 4 4L10.5 9l3 2.5-1.5 2C7 13 3 9 2.5 4z"/></svg></span>
        055-210 318 640
      </li>
      <li>
        <span class="icon"><svg viewBox="0 0 16 16"><rect x="4" y="2" width="8" height="4"/><rect x="2" y="6" width="12" height="5"/><rect x="4" y="10" width="8" height="4"/></svg></span>
        055-210 318 641
      </li>
      <li>
        <span class="icon"><svg viewBox="0 0 16 16"><rect x="2" y="4" width="12" height="8"/><path d="M2 4l6 5 6-5"/></svg></span>
        hello@marblecrest.co (Reception)
      </li>
      <li>
        <span class="icon"><svg viewBox="0 0 16 16"><rect x="2" y="4" width="12" height="8"/><path d="M2 4l6 5 6-5"/></svg></span>
        daniel@marblecrest.co (Direct)
      </li>
    </ul>

    <p class="address">421, Address line goes here<br>45452, Country Name</p>
    <p class="social">ig handle <span class="social__dot"></span></p>
  </section>

</body>
</html>
```